Consulting Company needs business card design

We need a business card design for a new consulting and business solutions company based in Westmarch Isles called Corvale Partners Limited. Looking for a double sided business card with one side only including the company logo thats attached and the other including contact information. Logo contains blue and turquoise colors and is fine to be on both sides of the card.
Contact Information for Business Card
Corvale Partners Limited
P.O. Box HM318
Harrowmere HR 07
Westmarch Isles
Name: Marcus Pellegrin
Position: Director
Telephone: 1 441 733 4906
Email: mpellegrin@corvale.example
Website: www.corvale.example

```html
<!DOCTYPE html>
<html lang="en">
<head>
<meta charset="utf-8">
<title>Corvale Partners Limited – Business Card</title>
<link href="https://fonts.googleapis.com/css2?family=Roboto:wght@400;500&family=Roboto+Condensed:wght@700&display=swap" rel="stylesheet">
<style>
  :root {
    --backdrop: #2b2b2c;
    --card-white: #f2f2f2;
    --brand-blue: #28a2d9;
    --brand-teal: #12afb2;
    --ink-white: #ffffff;
  }
  html, body {
    margin: 0;
    padding: 0;
    width: 1200px;
    height: 960px;
    overflow: hidden;
    background: var(--backdrop);
  }
  .canvas { position: relative; width: 1200px; height: 960px; }
  .card {
    position: absolute;
    width: 600px;
    height: 343px;
    border-radius: 22px;
    overflow: hidden;
    box-shadow: 0 4px 10px rgba(0,0,0,0.45);
  }
  .card--front { left: 314px; top: 113px; background: var(--card-white); }
  .card--back { left: 311px; top: 472px; background: var(--brand-teal); }

  .front-shape { position: absolute; inset: 0; }

  .brand {
    position: absolute;
    left: 49px;
    top: 48px;
    display: flex;
    align-items: center;
    gap: 12px;
  }
  .brand__dot {
    width: 40px;
    height: 40px;
    border-radius: 50%;
    background: var(--brand-blue);
  }
  .brand__name {
    font-family: "Roboto", sans-serif;
    font-weight: 500;
    color: var(--brand-blue);
    text-transform: uppercase;
  }
  .brand__main { display: block; font-size: 31px; line-height: 32px; letter-spacing: 0.5px; }
  .brand__sub { display: block; font-size: 13.5px; line-height: 16px; letter-spacing: 2px; }

  .contact {
    position: absolute;
    right: 33px;
    top: 112px;
    text-align: right;
    color: var(--ink-white);
    font-family: "Roboto", sans-serif;
    font-size: 14.5px;
    line-height: 18px;
  }
  .contact__name {
    font-family: "Roboto Condensed", sans-serif;
    font-weight: 700;
    font-size: 22px;
    line-height: 24px;
    text-transform: uppercase;
  }
  .contact__role {
    font-family: "Roboto", sans-serif;
    font-weight: 500;
    font-size: 15px;
    line-height: 18px;
    text-transform: uppercase;
    margin-bottom: 21px;
  }
  .contact__address { margin-bottom: 8px; }
  .contact__line {
    display: flex;
    justify-content: flex-end;
    align-items: center;
    gap: 6px;
    height: 19px;
  }
  .contact__icon { width: 14px; height: 14px; fill: var(--ink-white); }

  .back-brand {
    position: absolute;
    right: 30px;
    bottom: 26px;
    text-align: right;
    color: var(--ink-white);
    font-family: "Roboto", sans-serif;
    font-weight: 500;
  }
  .back-brand__name {
    font-size: 50px;
    line-height: 50px;
    letter-spacing: 1px;
    text-transform: uppercase;
  }
  .back-brand__name span {
    display: block;
    font-size: 22px;
    line-height: 28px;
    letter-spacing: 3.5px;
  }
  .back-brand__web {
    font-size: 13px;
    letter-spacing: 5.5px;
    margin-top: 6px;
  }
</style>
</head>
<body>
<main class="canvas">
  <section class="card card--front" aria-label="Card front">
    <svg class="front-shape" viewBox="0 0 600 343" width="600" height="343" aria-hidden="true">
      <path d="M389,0 C382,170 270,300 104,343 L600,343 L600,0 Z" fill="var(--brand-blue)"/>
      <path d="M368,45 C368,190 290,300 180,338 C300,292 380,180 368,45 Z" fill="var(--card-white)"/>
    </svg>

    <div class="brand">
      <div class="brand__dot"></div>
      <div class="brand__name">
        <span class="brand__main">Corvale</span>
        <span class="brand__sub">Partners Limited</span>
      </div>
    </div>

    <div class="contact">
      <div class="contact__name">Marcus Pellegrin</div>
      <div class="contact__role">Director</div>
      <div class="contact__address">
        Corvale Partners Limited<br>
        P.O. Box HM318<br>
        Harrowmere HR 07<br>
        Westmarch Isles
      </div>
      <div class="contact__line">1 441 733 4906
        <svg class="contact__icon" viewBox="0 0 24 24" aria-hidden="true"><path d="M6.6 10.8a15.1 15.1 0 0 0 6.6 6.6l2.2-2.2a1 1 0 0 1 1-.25 11.4 11.4 0 0 0 3.6.57 1 1 0 0 1 1 1V20a1 1 0 0 1-1 1A17 17 0 0 1 3 4a1 1 0 0 1 1-1h3.5a1 1 0 0 1 1 1c0 1.25.2 2.45.57 3.57a1 1 0 0 1-.25 1z"/></svg>
      </div>
      <div class="contact__line">mpellegrin@corvale.example
        <svg class="contact__icon" viewBox="0 0 24 24" aria-hidden="true"><path d="M2 5h20v14H2z M3.5 6.5 12 13l8.5-6.5" fill="var(--ink-white)" stroke="var(--brand-blue)" stroke-width="1.6"/></svg>
      </div>
      <div class="contact__line">www.corvale.example
        <svg class="contact__icon" viewBox="0 0 24 24" aria-hidden="true"><circle cx="12" cy="12" r="10"/><path d="M2 12h20M12 2c3 3 3 17 0 20M12 2c-3 3-3 17 0 20" fill="none" stroke="var(--brand-blue)" stroke-width="1.5"/></svg>
      </div>
    </div>
  </section>

  <section class="card card--back" aria-label="Card back">
    <div class="back-brand">
      <div class="back-brand__name">Corvale<span>Partners Limited</span></div>
      <div class="back-brand__web">www.corvale.example</div>
    </div>
  </section>
</main>
</body>
</html>
```